kestrelnet9 - a safety solution for schools

A Amok App for schools needs your help to design some screens. Its important to have a very simple use of the app. The function of the app is very easy, you put the button to trigger the alarm. The app has a message function. So we need 3 howto screens. you find a better description of the project in the briefing-file. If you have any questions just ask. Thanks in advance for the suggestions. Best Regards, Lars

Target Market(s)

Schools

Industry/Entity Type

Security Service

Font styles to use
Sans Serif

Colors

Designer to choose colors to be used in the design.

Requirements
Must have
• Simple, easy to use, look like a security app, trust,

```html
<!DOCTYPE html>
<html lang="de">
<head>
<meta charset="utf-8">
<title>kestrelnet9 – App Screens</title>
<link rel="stylesheet" href="https://fonts.googleapis.com/css2?family=Nunito+Sans:wght@400;600;700;800&display=swap">
<style>
  :root {
    --bg: #ffffff;
    --paper: #f7f7f7;
    --blue-light: #17b7fb;
    --blue: #1479f5;
    --orange: #f7941d;
    --yellow: #ffd000;
    --orange-deep: #ff8500;
    --red-light: #fb4a48;
    --red: #dd1015;
    --alarm-red: #ee2b2b;
    --grey-text: #666a70;
    --white: #ffffff;
    --green: #2ecc55;
  }
  * { box-sizing: border-box; margin: 0; padding: 0; }
  html, body { width: 1200px; height: 1200px; overflow: hidden; background: var(--bg); }
  body { position: relative; font-family: "Nunito Sans", Arial, sans-serif; }

  .screen {
    position: absolute; width: 230px; height: 500px;
    border-radius: 22px; overflow: hidden;
  }
  .screen--light { left: 137px; top: 40px; background: var(--paper); }
  .screen--blue { left: 468px; top: 40px; background: linear-gradient(180deg, var(--blue-light), var(--blue)); }
  .screen--messaging { left: 810px; top: 40px; background: linear-gradient(160deg, var(--yellow), var(--orange-deep)); }
  .screen--alarming { left: 468px; top: 638px; background: linear-gradient(180deg, var(--red-light), var(--red)); }

  .demo-header { position: absolute; left: 0; top: 0; width: 100%; height: 85px; padding: 32px 18px 0 26px; color: var(--white); }
  .screen--light .demo-header { background: linear-gradient(90deg, var(--blue-light), var(--blue)); }
  .screen--blue .demo-header { background: var(--orange); }
  .demo-header h2 { font-size: 12.5px; font-weight: 700; margin-bottom: 10px; }
  .demo-header p { font-size: 5.4px; font-weight: 700; line-height: 1.35; }

  .alarm-title { position: absolute; top: 104px; width: 100%; text-align: center; font-size: 13px; font-weight: 700; }
  .screen--light .alarm-title { color: var(--grey-text); }
  .screen--blue .alarm-title { color: var(--white); }

  .alarm-button { position: absolute; left: 41px; top: 146px; width: 150px; height: 150px; }

  .cancel-row { position: absolute; left: 0; width: 100%; text-align: center; font-size: 10px; font-weight: 600; color: var(--alarm-red); }
  .screen--light .cancel-row { top: 344px; }
  .screen--blue .cancel-row { top: 334px; }
  .cancel-row .count { margin-right: 14px; }

  .menu-button {
    position: absolute; left: 34px; width: 166px; height: 28px; border-radius: 14px;
    display: flex; align-items: center; justify-content: center; font-size: 10px; font-weight: 600;
  }
  .menu-button svg { position: absolute; left: 13px; top: 7px; width: 14px; height: 14px; }
  .menu-button--message { top: 386px; }
  .menu-button--settings { top: 440px; }
  .screen--light .menu-button { background: var(--blue); color: var(--white); box-shadow: 0 4px 8px rgba(20,121,245,.25); }
  .screen--blue .menu-button { background: var(--white); color: var(--grey-text); box-shadow: 0 4px 8px rgba(0,0,0,.12); }

  .howto-header { position: absolute; top: 34px; width: 100%; text-align: center; color: var(--white); font-size: 12.5px; font-weight: 700; }
  .back-arrow { position: absolute; left: 24px; top: 37px; width: 18px; height: 14px; }
  .howto-illustration { position: absolute; left: 38px; top: 132px; width: 154px; height: 120px; border-radius: 14px; background: var(--white); }
  .howto-headline { position: absolute; top: 338px; width: 100%; text-align: center; color: var(--white); font-size: 6.8px; font-weight: 700; }
  .howto-body { position: absolute; left: 14px; right: 14px; top: 367px; color: rgba(255,255,255,.85); font-size: 6.6px; line-height: 1.35; }
  .pager { position: absolute; top: 463px; width: 100%; display: flex; justify-content: center; gap: 14px; }
  .pager span { width: 5px; height: 5px; border-radius: 50%; background: rgba(255,255,255,.55); }
  .pager span.is-active { background: var(--white); }
</style>
</head>
<body>

<svg width="0" height="0" style="position:absolute">
  <defs>
    <symbol id="bell" viewBox="0 0 100 100">
      <g fill="none" stroke="var(--alarm-red)" stroke-width="5" stroke-linecap="round" stroke-linejoin="round">
        <path d="M50 12 v8"/>
        <path d="M28 72 V48 a22 24 0 0 1 44 0 V72"/>
        <path d="M16 80 Q28 74 28 72 H72 Q72 74 84 80 Z"/>
        <path d="M43 82 a7 7 0 0 0 14 0"/>
        <path d="M56 34 a12 12 0 0 1 6 10"/>
      </g>
    </symbol>
  </defs>
</svg>

<section class="screen screen--light">
  <header class="demo-header">
    <h2>Demo Modus</h2>
    <p>The function of the app is very easy, you put the button to trigger the alarm. The app has a message function.</p>
  </header>
  <h1 class="alarm-title">Schul-Alarm auslösen</h1>
  <svg class="alarm-button" viewBox="0 0 150 150">
    <circle cx="75" cy="75" r="70" fill="var(--paper)" style="filter:drop-shadow(0 10px 12px rgba(0,0,0,.12))"/>
    <path d="M75 2 A73 73 0 0 1 75 148" fill="none" stroke="var(--alarm-red)" stroke-width="3"/>
    <use href="#bell" x="37" y="37" width="76" height="76"/>
  </svg>
  <p class="cancel-row"><span class="count">09</span>Alarm abbrechen</p>
  <div class="menu-button menu-button--message">
    <svg viewBox="0 0 16 16" fill="none" stroke="currentColor" stroke-width="1.4"><path d="M2 2.5h12v9H6l-4 3z" stroke-linejoin="round"/></svg>
    Message
  </div>
  <div class="menu-button menu-button--settings">
    <svg viewBox="0 0 16 16"><circle cx="8" cy="8" r="5" fill="none" stroke="currentColor" stroke-width="3" stroke-dasharray="2.2 1.7"/><circle cx="8" cy="8" r="4" fill="currentColor"/><circle cx="8" cy="8" r="1.6" fill="var(--blue)"/></svg>
    Settings
  </div>
</section>

<section class="screen screen--blue">
  <header class="demo-header">
    <h2>Demo Modus</h2>
    <p>The function of the app is very easy, you put the button to trigger the alarm. The app has a message function.</p>
  </header>
  <h1 class="alarm-title">Schul-Alarm auslösen</h1>
  <svg class="alarm-button" viewBox="0 0 150 150">
    <circle cx="75" cy="75" r="72" fill="#bde3f8" style="filter:drop-shadow(0 10px 12px rgba(0,40,120,.25))"/>
    <path d="M75 2 A73 73 0 0 1 75 148" fill="none" stroke="var(--alarm-red)" stroke-width="3"/>
    <use href="#bell" x="37" y="37" width="76" height="76"/>
  </svg>
  <p class="cancel-row"><span class="count">09</span>Alarm abbrechen</p>
  <div class="menu-button menu-button--message">
    <svg viewBox="0 0 16 16" fill="none" stroke="var(--green)" stroke-width="1.4"><path d="M2 2.5h12v9H6l-4 3z" stroke-linejoin="round"/></svg>
    Message
  </div>
  <div class="menu-button menu-button--settings">
    <svg viewBox="0 0 16 16"><circle cx="8" cy="8" r="5" fill="none" stroke="var(--green)" stroke-width="3" stroke-dasharray="2.2 1.7"/><circle cx="8" cy="8" r="4" fill="var(--green)"/><circle cx="8" cy="8" r="1.6" fill="var(--white)"/></svg>
    Settings
  </div>
</section>

<section class="screen screen--messaging">
  <svg class="back-arrow" viewBox="0 0 18 14" fill="none" stroke="var(--white)" stroke-width="1.5" stroke-linecap="round"><path d="M17 7H2M7 1.5 1.5 7 7 12.5"/></svg>
  <h1 class="howto-header">Messaging</h1>
  <div class="howto-illustration" role="img" aria-label="Illustration of a message envelope being sent"></div>
  <p class="howto-headline">It shows how you can trigger an alarm</p>
  <p class="howto-body">Lorem ipsum dolor sit amet, consectetur adipisicing elit, sed do eiusmod tempor incididunt ut labore et dolore magna aliqua. Ut enim ad minim veniam, quis nostrud excepteur sint occaecat</p>
  <div class="pager"><span></span><span class="is-active"></span><span></span></div>
</section>

<section class="screen screen--alarming">
  <svg class="back-arrow" viewBox="0 0 18 14" fill="none" stroke="var(--white)" stroke-width="1.5" stroke-linecap="round"><path d="M17 7H2M7 1.5 1.5 7 7 12.5"/></svg>
  <h1 class="howto-header">Alarming</h1>
  <div class="howto-illustration" role="img" aria-label="Illustration of a ringing alarm bell with a thumbs-up"></div>
  <p class="howto-headline">It shows how you can trigger an alarm</p>
  <p class="howto-body">Lorem ipsum dolor sit amet, consectetur adipisicing elit, sed do eiusmod tempor incididunt ut labore et dolore magna aliqua. Ut enim ad minim veniam, quis nostrud excepteur sint occaecat</p>
  <div class="pager"><span></span><span class="is-active"></span><span></span></div>
</section>

</body>
</html>
```